Business card design for new eCommerce site focusing on integrity and strong businsess tactics

We need a business card that will stand out and be memorable. Something with color that matches our company logo colors. Think high end version of Dealvine. There are 2 logos provided. The parent company is called Bright Harbor Ventures and we are presenting a new and very exciting eCommerce site called KeenTraders.example.

Target Market(s)

Our target markets are in the Activities, Food and Beverage, Health and Beauty

Industry/Entity Type

Marketing

Contact Information for Business Card

We have 4 members that need cards...I will provide all info to the winner of the design contest
Business Address is
48730 West 61st Avenue, Suite C204
Phoenix AZ 85917

Font styles to use
Serif
Sans Serif

Colors

Designer to choose colors to be used in the design.

Requirements
Must have
• The card must be memorable...should be unique in design but must exude integrity and be playful .
• I have provided several colors or our parent company...please feel free to use which ever
Nice to have
• I will leave this up to you. Feel free to use other images of your choosing that wraps around our client.....Activities, Dining, Health, Beauty
Should not have
• just dont be boring

```html
<!DOCTYPE html>
<html lang="en">
<head>
<meta charset="utf-8">
<title>KeenTraders.example Business Card</title>
<link href="https://fonts.googleapis.com/css2?family=Mulish:wght@400;700;800&display=swap" rel="stylesheet">
<style>
  :root {
    --navy: #141d4a;
    --navy-light: #1f2a5e;
    --green: #7dc242;
    --blue: #2f7fc0;
    --grey-text: #6d6d6d;
    --card-white: #ffffff;
    --backdrop: #e4e4e4;
    --tagline-dark: #4a4a4a;
  }
  * { margin: 0; padding: 0; box-sizing: border-box; }
  html, body {
    width: 1200px; height: 1000px; overflow: hidden;
    background: var(--backdrop);
    font-family: "Mulish", Arial, sans-serif;
  }
  .canvas { position: relative; width: 1200px; height: 1000px; }
  .card {
    position: absolute; left: 270px; width: 660px; height: 380px;
    border-radius: 22px; overflow: hidden;
    box-shadow: 0 6px 14px rgba(0,0,0,0.25);
  }
  .card-front { top: 108px; background: linear-gradient(135deg, var(--navy) 0%, var(--navy-light) 55%, var(--navy) 100%); }
  .card-back { top: 520px; background: var(--card-white); }

  .brand { position: absolute; display: flex; align-items: center; }
  .brand-dot { border-radius: 50%; background: var(--blue); flex-shrink: 0; }
  .brand-name { font-weight: 700; color: var(--green); letter-spacing: -0.3px; white-space: nowrap; line-height: 1; }
  .tagline { position: absolute; white-space: nowrap; letter-spacing: 1px; line-height: 1; }

  .card-front .brand { left: 110px; top: 171px; }
  .card-front .brand-dot { width: 44px; height: 44px; margin-right: 68px; }
  .card-front .brand-name { font-size: 33px; }
  .card-front .tagline { left: 224px; top: 210px; font-size: 17.5px; color: #ffffff; }

  .card-back .brand { left: 38px; top: 72px; }
  .card-back .brand-dot { width: 40px; height: 40px; margin-right: 52px; }
  .card-back .brand-name { font-size: 28px; }
  .card-back .tagline { left: 131px; top: 107px; font-size: 14.5px; color: var(--tagline-dark); }

  .contact { position: absolute; left: 36px; top: 183px; color: var(--grey-text); font-size: 14.5px; line-height: 20px; }
  .contact-name { font-size: 19px; font-weight: 700; color: var(--green); line-height: 22px; }
  .contact-title { margin-bottom: 10px; }
  .contact-address { margin-bottom: 14px; }
  .contact-line { display: flex; align-items: center; gap: 4px; height: 27px; }
  .contact-line svg { width: 16px; height: 16px; }

  .parent-brand { position: absolute; left: 426px; top: 200px; width: 216px; text-align: center; }
  .parent-circle { width: 96px; height: 96px; border-radius: 50%; background: var(--navy); margin: 0 auto 10px; border: 3px solid var(--card-white); box-shadow: 0 0 0 2px var(--navy); }
  .parent-name { font-size: 17px; font-weight: 800; color: var(--navy); white-space: nowrap; }

  .stripe-green { position: absolute; left: 0; right: 0; bottom: 14px; height: 3px; background: var(--green); }
  .stripe-blue { position: absolute; left: 0; right: 0; bottom: 0; height: 11px; background: var(--blue); }
</style>
</head>
<body>
<div class="canvas">
  <section class="card card-front">
    <div class="brand">
      <span class="brand-dot"></span>
      <span class="brand-name">KeenTraders.example</span>
    </div>
    <div class="tagline">Activities-Dining-Health-Beauty</div>
  </section>

  <section class="card card-back">
    <div class="brand">
      <span class="brand-dot"></span>
      <span class="brand-name">KeenTraders.example</span>
    </div>
    <div class="tagline">Activities-Dining-Health-Beauty</div>

    <div class="contact">
      <div class="contact-name">Elias Brandt</div>
      <div class="contact-title">Managing Director</div>
      <div class="contact-address">48730 West 61st Avenue, Suite C204<br>Phoenix AZ 85917</div>
      <div class="contact-line">
        <svg viewBox="0 0 16 16"><circle cx="8" cy="8" r="7" fill="none" stroke="#2f7fc0" stroke-width="1.4"/><path d="M5.5 4.5c-.6.6-.5 2 .8 3.6s3 2.6 3.8 1.9l.6-.7-1.4-1.1-.7.6c-.6-.2-1.6-1.2-1.8-1.8l.6-.7-1.1-1.4z" fill="#2f7fc0"/></svg>
        <span>+61 400 555 012</span>
      </div>
      <div class="contact-line">
        <svg viewBox="0 0 16 16"><circle cx="8" cy="8" r="7" fill="none" stroke="#2f7fc0" stroke-width="1.4"/><rect x="4.2" y="5.2" width="7.6" height="5.6" fill="none" stroke="#2f7fc0" stroke-width="1.1"/><path d="M4.2 5.2 8 8.4l3.8-3.2" fill="none" stroke="#2f7fc0" stroke-width="1.1"/></svg>
        <span>info@KeenTraders.example</span>
      </div>
    </div>

    <div class="parent-brand">
      <div class="parent-circle"></div>
      <div class="parent-name">Bright Harbor Ventures</div>
    </div>

    <div class="stripe-green"></div>
    <div class="stripe-blue"></div>
  </section>
</div>
</body>
</html>
```